kestrova business cards

Hey design gurus!
I'm after a clean, modern, stylish business card for my about to be launched company.
I've uploaded the logos for my company "Kestrova Electrical Solutions"
and also the tarrow alliance logo to whom i am associated.

```html
<!DOCTYPE html>
<html lang="en">
<head>
<meta charset="utf-8">
<title>Kestrova Electrical Solutions – Business Cards</title>
<link rel="stylesheet" href="https://fonts.googleapis.com/css2?family=Michroma&family=Poppins:wght@400&display=swap">
<style>
  :root {
    --backdrop: #c9c9c9;
    --card-white: #ffffff;
    --ink-dark: #03141d;
    --brand-blue: #0a76c6;
    --brand-blue-light: #1886d4;
    --brand-blue-deep: #0a63a8;
    --line-white: #ffffff;
    --text-dark: #1b1b1b;
  }
  * { margin: 0; padding: 0; box-sizing: border-box; }
  html, body { width: 772px; height: 1200px; overflow: hidden; }
  body { background: var(--backdrop); position: relative; }

  .card {
    position: absolute;
    top: 302px;
    width: 340px;
    height: 595px;
    overflow: hidden;
    box-shadow: 6px 8px 14px rgba(0,0,0,0.35);
  }
  .card--front { left: 31px; background: var(--card-white); }
  .card--back { left: 401px; background: var(--ink-dark); }

  .card__inner {
    position: absolute;
    left: 0; top: 0;
    width: 577px; height: 1010px;
    transform: scale(0.5893);
    transform-origin: 0 0;
  }
  .card__art { position: absolute; left: 0; top: 0; width: 577px; height: 1010px; }

  .holder-name {
    position: absolute; left: 0; width: 577px; text-align: center;
    font-family: "Michroma", sans-serif; line-height: 1;
  }
  .holder-name--first { top: 80px; font-size: 47px; color: var(--text-dark); }
  .holder-name--last { top: 124px; font-size: 50px; color: var(--brand-blue); letter-spacing: -1px; }
  .holder-role {
    position: absolute; left: 0; width: 577px; top: 182px; text-align: center;
    font-family: "Michroma", sans-serif; font-size: 20px; letter-spacing: 10px;
    color: var(--text-dark); padding-left: 10px;
  }

  .contact {
    position: absolute; left: 0; width: 577px; text-align: center;
    font-family: "Poppins", sans-serif; font-size: 25px; color: var(--text-dark); line-height: 34px;
  }
  .contact--phone { top: 510px; }
  .contact--email { top: 601px; }
  .contact--address { top: 687px; }
  .contact-icon { position: absolute; left: 276px; width: 24px; height: 24px; }
  .contact-icon--phone { top: 484px; }
  .contact-icon--email { top: 578px; }
  .contact-icon--pin { top: 660px; }

  .wordmark {
    position: absolute; text-align: center;
    font-family: "Michroma", sans-serif; color: var(--brand-blue); line-height: 1;
  }
  .wordmark__name { display: block; font-size: 32px; letter-spacing: 1px; }
  .wordmark__tag { display: block; font-size: 12px; letter-spacing: 3px; margin-top: 6px; }
  .wordmark--front { left: 138px; width: 300px; top: 912px; }
  .wordmark--back { left: 178px; width: 330px; top: 476px; text-align: left; }
  .wordmark--back .wordmark__name { font-size: 34px; }
  .wordmark--back .wordmark__tag { font-size: 12.5px; letter-spacing: 3.4px; padding-left: 4px; }
</style>
</head>
<body>

<section class="card card--front" aria-label="Business card front">
  <div class="card__inner">
    <svg class="card__art" viewBox="0 0 577 1010" xmlns="http://www.w3.org/2000/svg">
      <defs>
        <linearGradient id="cableFront" x1="0" y1="0" x2="1" y2="1">
          <stop offset="0" stop-color="#1886d4"/>
          <stop offset="1" stop-color="#0a6bb6"/>
        </linearGradient>
      </defs>
      <rect class="cable-illustration" x="175" y="268" width="265" height="205" rx="70" fill="url(#cableFront)" role="img" aria-label="Coiled blue electric cable ending in a plug"/>
      <path d="M0 961 A311 311 0 0 1 175 784" fill="none" stroke="var(--brand-blue)" stroke-width="3"/>
      <path d="M395 784 A311 311 0 0 1 577 953" fill="none" stroke="var(--brand-blue)" stroke-width="3"/>
      <circle cx="290" cy="1073" r="253" fill="var(--ink-dark)"/>
    </svg>

    <div class="holder-name holder-name--first">DALEN</div>
    <div class="holder-name holder-name--last">MARSH</div>
    <div class="holder-role">OWNER</div>

    <svg class="contact-icon contact-icon--phone" viewBox="0 0 24 24" aria-hidden="true">
      <path d="M6.6 10.8a15 15 0 0 0 6.6 6.6l2.2-2.2c.3-.3.7-.4 1-.2 1.1.4 2.3.6 3.6.6.6 0 1 .4 1 1V20c0 .6-.4 1-1 1A17 17 0 0 1 3 4c0-.6.4-1 1-1h3.5c.6 0 1 .4 1 1 0 1.3.2 2.5.6 3.6.1.3 0 .7-.2 1z" fill="var(--brand-blue)"/>
    </svg>
    <div class="contact contact--phone">+234 5812 4473</div>

    <svg class="contact-icon contact-icon--email" viewBox="0 0 24 24" aria-hidden="true">
      <rect x="1" y="5" width="22" height="15" fill="var(--brand-blue)"/>
      <path d="M1 5 L12 13 L23 5 M1 20 L9 11 M23 20 L15 11" fill="none" stroke="#fff" stroke-width="1.5"/>
    </svg>
    <div class="contact contact--email">info@kestrova.com</div>

    <svg class="contact-icon contact-icon--pin" viewBox="0 0 24 24" aria-hidden="true">
      <path d="M12 1a8 8 0 0 0-8 8c0 6 8 14 8 14s8-8 8-14a8 8 0 0 0-8-8z" fill="var(--brand-blue)"/>
      <circle cx="12" cy="9" r="3" fill="#fff"/>
    </svg>
    <div class="contact contact--address">48B Street 9 Harbour Road,<br>Las Vegas</div>

    <div class="wordmark wordmark--front">
      <span class="wordmark__name">KESTROVA</span>
      <span class="wordmark__tag">ELECTRICAL SOLUTIONS</span>
    </div>
  </div>
</section>

<section class="card card--back" aria-label="Business card back">
  <div class="card__inner">
    <svg class="card__art" viewBox="0 0 577 1010" xmlns="http://www.w3.org/2000/svg">
      <defs>
        <linearGradient id="cableBack" x1="0" y1="0" x2="1" y2="1">
          <stop offset="0" stop-color="#1886d4"/>
          <stop offset="1" stop-color="#0a6bb6"/>
        </linearGradient>
      </defs>
      <rect class="cable-illustration" x="180" y="145" width="250" height="185" rx="65" fill="url(#cableBack)" role="img" aria-label="Coiled blue electric cable ending in a plug"/>

      <circle class="mark-dot" cx="123" cy="497" r="36" fill="none" stroke="var(--brand-blue)" stroke-width="5"/>

      <path d="M0 961 A311 311 0 0 1 175 784" fill="none" stroke="var(--line-white)" stroke-width="3"/>
      <path d="M395 784 A311 311 0 0 1 577 953" fill="none" stroke="var(--line-white)" stroke-width="3"/>
      <circle cx="290" cy="1073" r="253" fill="var(--brand-blue)"/>

      <rect class="partner-badge" x="180" y="877" width="215" height="76" rx="6" fill="none" stroke="var(--line-white)" stroke-width="2" role="img" aria-label="Tarrow Alliance partner badge"/>
    </svg>

    <div class="wordmark wordmark--back">
      <span class="wordmark__name">KESTROVA</span>
      <span class="wordmark__tag">ELECTRICAL SOLUTIONS</span>
    </div>
  </div>
</section>

</body>
</html>
```